Re-style home page - eye-catching and unique design for social commerce website

We need a new concept design for TrindaMo's home page.
We don't want to make huge changes but creating a more professional and eye-catching style.

We need to look very serious like a professional services company and in the same time to look like a social network for e-commerce.

Our logo is very captive and you can use to creating something of harmonious.

This is a re-style and I'm excepted to see unique and fresh design like Clovaret.

Target Market(s)

e-commerce and social

Industry/Entity Type

Social

Number of Pages Required

1 page

Font styles to use
Serif
Sans Serif

Requirements
Must have
• An eye-catching result.
• Search bar with logo and Login How it works and business
• The slogan with login and signup.
• Footer links.
Nice to have
• I would like to open the home page and see only two clear ways:
• -Consumer
• --Search
• --The slogan
• --Login and Signup
• --How it works
• -Business
• --Go to Business area
• Background: City, Shopping.
Should not have
• Scrollbar style!

```html
<!DOCTYPE html>
<html lang="en">
<head>
<meta charset="utf-8">
<title>TrindaMo – Shop directly from your profile</title>
<link href="https://fonts.googleapis.com/css2?family=Montserrat:wght@500;600;700&family=Open+Sans:wght@400;600;700&display=swap" rel="stylesheet">
<style>
:root{
  --bar:#2a2a2a;
  --white:#ffffff;
  --ink:#111111;
  --orange:#ef9a3e;
  --panel:rgba(236,238,242,0.72);
  --slogan:#d3325a;
  --social:#3a5a9e;
  --social-dark:#2f4b87;
  --join:#f7b500;
  --t-red:#d63c5e;
  --t-blue:#3c4fcf;
  --t-amber:#f0a51c;
  --t-coral:#f0663f;
  --t-tan:#eb9a3c;
  --t-periwinkle:#7e86e8;
  --t-olive:#b5c86b;
  --t-lilac:#8a86e6;
  --t-rose:#e0405a;
  --t-lemon:#eed43e;
  --t-yellow:#f5c11e;
  --t-sage:#c3c56c;
  --t-slate:#5b6192;
  --t-salmon:#f79c88;
  --t-tomato:#f56a3f;
  --t-mustard:#bb9f27;
  --t-crimson:#d03256;
}
*{box-sizing:border-box;margin:0;padding:0}
html,body{width:1200px;height:861px;overflow:hidden}
body{position:relative;font-family:"Open Sans",Arial,sans-serif;color:var(--white);background:#8d8f96}
.city-backdrop{position:absolute;inset:0;
  background:
   radial-gradient(ellipse 180px 420px at 120px 420px,rgba(30,30,40,.55),transparent 70%),
   radial-gradient(ellipse 200px 420px at 1080px 420px,rgba(30,40,60,.5),transparent 70%),
   radial-gradient(ellipse 120px 200px at 930px 260px,rgba(220,120,150,.45),transparent 70%),
   linear-gradient(180deg,#6f737d 0%,#9a9ca3 45%,#b7b8bc 75%,#a6a7ab 100%);}
.topbar{position:absolute;left:0;top:0;width:1200px;height:67px;background:rgba(42,42,42,.92)}
.brand{position:absolute;left:110px;top:10px;display:flex;align-items:center;gap:10px;
  font-family:"Montserrat",Arial,sans-serif;font-weight:700;font-size:40px;color:var(--white);letter-spacing:-.5px}
.brand-mark{width:16px;height:16px;background:var(--orange);border-radius:50%}
.search{position:absolute;left:562px;top:16px;width:236px;height:34px;display:flex}
.search-field{flex:1;background:var(--white);border-radius:3px 0 0 3px;font-size:12px;color:#9a9a9a;padding:9px 10px}
.search-button{width:36px;background:var(--orange);border-radius:0 3px 3px 0;display:flex;align-items:center;justify-content:center}
.main-nav{position:absolute;top:23px;left:824px;display:flex;font-family:"Montserrat",Arial,sans-serif;font-weight:600;font-size:15px}
.main-nav a{color:var(--white);text-decoration:none}
.nav-login{margin-right:33px}.nav-how{margin-right:37px}
.headline{position:absolute;top:142px;left:0;width:1200px;text-align:center;font-family:"Montserrat",Arial,sans-serif;font-weight:600;font-size:27px;letter-spacing:.3px}
.feed-panel{position:absolute;left:277px;top:195px;width:647px;height:551px;background:var(--panel);border-radius:4px;box-shadow:0 3px 14px rgba(0,0,0,.35)}
.feed-title{position:absolute;top:20px;width:100%;text-align:center;font-family:"Montserrat",Arial,sans-serif;font-weight:600;font-size:25px;color:var(--ink)}
.category-grid{position:absolute;left:36px;top:70px;width:576px;display:grid;grid-template-columns:repeat(5,1fr);grid-auto-rows:92px}
.tile{display:flex;flex-direction:column;align-items:center;justify-content:flex-end;padding-bottom:18px;text-align:center;font-size:13.5px;line-height:17px;text-transform:uppercase;color:var(--white);gap:6px}
.tile svg{width:38px;height:38px;fill:none;stroke:var(--white);stroke-width:2.4;stroke-linecap:round;stroke-linejoin:round}
.tile.two-line{padding-bottom:8px}
.member{justify-content:center;padding:0;font-size:14px;gap:4px}
.join-button{background:var(--join);color:var(--ink);text-transform:none;font-size:12px;font-weight:600;padding:1px 11px;border-radius:2px;border:1px solid #d99a00}
.slogan{position:absolute;top:452px;width:100%;text-align:center;font-family:"Montserrat",Arial,sans-serif;font-weight:700;font-size:25px;color:var(--slogan);letter-spacing:-.3px}
.social-login{position:absolute;left:220px;top:493px;width:206px;height:43px;border-radius:4px;background:linear-gradient(#4a6bb0,var(--social-dark));display:flex;align-items:center;box-shadow:0 1px 2px rgba(0,0,0,.3)}
.social-login .mark{width:40px;height:100%;display:flex;align-items:center;justify-content:center;border-right:1px solid rgba(255,255,255,.25)}
.social-login .mark span{width:14px;height:14px;background:var(--white)}
.social-login .label{flex:1;text-align:center;font-size:13px;font-weight:600}
.footer{position:absolute;left:0;top:805px;width:1200px;height:56px;background:var(--bar);font-size:13px}
.copyright{position:absolute;left:110px;top:20px}
.footer-links{position:absolute;right:110px;top:20px}
.footer-links a{color:var(--white);text-decoration:none}
.footer-links .divider{margin:0 9px}
</style>
</head>
<body>
<div class="city-backdrop" role="img" aria-label="Blurred photo of shoppers walking along a busy city street"></div>

<header class="topbar">
  <div class="brand">TrindaMo<span class="brand-mark"></span></div>
  <div class="search">
    <div class="search-field">Search</div>
    <div class="search-button"><svg width="18" height="18" viewBox="0 0 18 18" fill="none" stroke="#fff" stroke-width="2"><circle cx="10.5" cy="7.5" r="5"/><path d="M7 11l-5 5"/></svg></div>
  </div>
  <nav class="main-nav"><a class="nav-login" href="#">Login</a><a class="nav-how" href="#">How it works</a><a href="#">Business</a></nav>
</header>

<h1 class="headline">SHOP DIRECTLY FROM YOUR PROFILE</h1>

<section class="feed-panel">
  <h2 class="feed-title">SETUP YOUR FEED</h2>
  <div class="category-grid">
    <div class="tile" style="background:var(--t-red)"><svg viewBox="0 0 40 40"><path d="M8 22h10l6-10 8 8"/><path d="M18 22l-4 10"/><circle cx="28" cy="8" r="3"/></svg>Active Life</div>
    <div class="tile" style="background:var(--t-blue)"><svg viewBox="0 0 40 40"><path d="M14 4v10M10 4v8a4 4 0 008 0V4M14 16v20"/><path d="M27 36V4c-4 4-4 12 0 16"/></svg>Food</div>
    <div class="tile" style="background:var(--t-amber)"><svg viewBox="0 0 40 40"><path d="M6 20l6-10h16l6 10v8H6z"/><circle cx="12" cy="28" r="3"/><circle cx="28" cy="28" r="3"/></svg>Automotive</div>
    <div class="tile" style="background:var(--t-coral)"><svg viewBox="0 0 40 40"><path d="M20 5c6 9 10 14 10 20a10 10 0 01-20 0c0-6 4-11 10-20z"/></svg>Beauty &amp; Spa</div>
    <div class="tile" style="background:var(--t-tan)"><svg viewBox="0 0 40 40"><path d="M3 15l17-8 17 8-17 8z"/><path d="M10 19v9c6 4 14 4 20 0v-9M35 16v10"/></svg>Education</div>

    <div class="tile two-line" style="background:var(--t-periwinkle)"><svg viewBox="0 0 40 40"><rect x="5" y="8" width="30" height="26" rx="2"/><path d="M5 15h30M12 4v7M28 4v7M11 21h4M18 21h4M25 21h4M11 27h4M18 27h4"/></svg>Event Planing<br>&amp; Services</div>
    <div class="tile two-line" style="background:var(--t-olive)"><svg viewBox="0 0 40 40"><circle cx="20" cy="18" r="12"/><path d="M24 13h-6a3 3 0 000 6h4a3 3 0 010 6h-6M20 10v3M20 25v3"/></svg>Financial<br>Services</div>
    <div class="tile two-line" style="background:var(--t-lilac)"><svg viewBox="0 0 40 40"><rect x="8" y="5" width="24" height="20"/><path d="M14 25l-5 11M26 25l5 11M20 25v8"/></svg>Art &amp;<br>Entertainment</div>
    <div class="tile two-line" style="background:var(--t-rose)"><svg viewBox="0 0 40 40"><path d="M20 33S5 24 5 14a7 7 0 0115-3 7 7 0 0115 3c0 10-15 19-15 19z"/><path d="M15 18h3l2-4 2 7 2-3h3"/></svg>Health &amp;<br>Medical</div>
    <div class="tile two-line" style="background:var(--t-lemon)"><svg viewBox="0 0 40 40"><circle cx="20" cy="20" r="6"/><path d="M20 5v6M20 29v6M5 20h6M29 20h6M9 9l4 4M27 27l4 4M31 9l-4 4M13 27l-4 4"/></svg>Local<br>Services</div>

    <div class="tile" style="background:var(--t-tan)"><svg viewBox="0 0 40 40"><rect x="11" y="8" width="18" height="28"/><path d="M15 13h2M23 13h2M15 19h2M23 19h2M15 25h2M23 25h2M18 36v-5h4v5"/></svg>Hotels</div>
    <div class="tile" style="background:var(--t-yellow)"><svg viewBox="0 0 40 40"><path d="M4 20L20 6l16 14M9 16v18h22V16"/><path d="M17 34v-9h6v9"/></svg>Home Services</div>
    <div class="tile" style="background:var(--t-sage)"><svg viewBox="0 0 40 40"><rect x="5" y="11" width="30" height="21" rx="2"/><path d="M14 4l6 7 6-7M15 36h10"/></svg>Mass Media</div>
    <div class="tile" style="background:var(--t-slate)"><svg viewBox="0 0 40 40"><path d="M16 30V8l16-4v22"/><circle cx="12" cy="30" r="4"/><circle cx="28" cy="26" r="4"/></svg>Night Life</div>
    <div class="tile" style="background:var(--t-salmon)"><svg viewBox="0 0 40 40"><path d="M8 34V18l12-10 12 10v16z"/><circle cx="20" cy="24" r="4"/></svg>Pets</div>

    <div class="tile" style="background:var(--t-salmon)"><svg viewBox="0 0 40 40"><path d="M3 20L16 8l13 12M7 17v15h18V17"/><path d="M30 22h7v12h-7z"/></svg>Real Estate</div>
    <div class="tile" style="background:var(--t-tomato)"><svg viewBox="0 0 40 40"><path d="M6 28a14 14 0 0128 0zM3 32h34M20 11v3"/></svg>Restaurants</div>
    <div class="tile two-line" style="background:var(--t-slate)"><svg viewBox="0 0 40 40"><rect x="5" y="12" width="30" height="21" rx="2"/><path d="M15 12V7h10v5M5 21h30"/></svg>Proessional<br>Services</div>
    <div class="tile two-line" style="background:var(--t-mustard)"><svg viewBox="0 0 40 40"><rect x="11" y="4" width="18" height="26" rx="3"/><path d="M11 17h18M14 36l3-6M26 36l-3-6"/><circle cx="15" cy="24" r="1"/><circle cx="25" cy="24" r="1"/></svg>Public Servces<br>&amp; Government</div>
    <div class="tile member" style="background:var(--t-crimson)">Become a<br>Member<span class="join-button">Join Now</span></div>
  </div>

  <p class="slogan">SAVE YOUR TIME LIVE BETTER</p>
  <a class="social-login" href="#"><span class="mark"><span></span></span><span class="label">Login with Linkora</span></a>
</section>

<footer class="footer">
  <p class="copyright">© 2015 trindamo.com.All Rights Reserved.</p>
  <p class="footer-links"><a href="#">Terms &amp; Condition</a><span class="divider">|</span><a href="#">Privacy Policy</a></p>
</footer>
</body>
</html>
```